Book Cover for Cyber Compliance Book

I need to get a book cover designed for use on "Pagewell Print Portal" - template attached.

The name of the book is: Charting KELMOR

Tagline: A Boardroom Leader’s Field Guide to Oversight and Endurance

Author: Martin J Hollis

Photo of author is attached and a logo for the QBWLN publishing organisation.

Please note: the author is high profile in the cyber security industry and use of his image and name on the book will help online sales.

I am open to changing the amount of copy used on the front and back of the book.

The book is about a European regulation for the financial sector called DORA Digital Operational Resilience Act. It is aimed at corporate level executives within the financial sector and the imagery should include relevant elements such as the EU, Financial sector, digital operations and cybersecurity.

I want to find an imaginative designer than can create something special and appealing.

I am not clear on exactly how many pages will be in the book so the template details may change slightly as the number becomes clear for the width of the spine etc. I will require all the template files used so I can make minor edits in AI or Photoshop

Note I can get the photo and attached logo in higher resolution if required

If possible I would like to see a 3D mockup of the book

Synopsis of Book:

n the ever-evolving landscape of financial services, the Digital Operational Resilience Act (DORA) stands as a beacon of change, ushering in a new era of regulatory requirements aimed at fortifying the digital fortitude of the sector. “Charting KELMOR: A Boardroom Leader’s Field Guide to Oversight and Endurance” is an indispensable guide tailored for leaders who are steering their organisations through the complexities of DORA compliance.
This comprehensive manual delves into the intricacies of DORA, elucidating the rationale behind its inception – the need for a unified and robust approach to managing ICT risks that have become increasingly prevalent in today’s interconnected financial ecosystem. The book offers a granular analysis of the five pillars central to DORA: ICT Risk Management, ICT-related Incident Management, Digital Operational Resilience Testing, ICT Third Party Risk Management, and Information Sharing Arrangements.
For financial entities and ICT service providers operating within the EU and beyond, “Charting KELMOR” serves as a strategic compass. It provides actionable insights into aligning with DORA’s standards, ensuring not just compliance but also a competitive edge in the EU market. The guide highlights the strategic importance of continuous learning and the emergence of specialized roles such as DORA Compliance Specialists, addressing the skills gap and career opportunities within this new regulatory framework.
The book also offers a detailed walkthrough of the Union-wide Oversight Framework, a novel aspect of DORA that places critical ICT third-party providers under direct regulatory scrutiny. It outlines the necessary steps for financial entities to ensure seamless collaboration with these providers, including the integration of specific contractual obligations to uphold DORA’s stringent resilience standards.
With practical advice and real-world scenarios, “Charting KELMOR” equips executives with the knowledge to conduct thorough DORA Compliance Assessments, map dependencies, and engage in scenario testing that aligns with the act’s rigorous testing regimen. It is not just a guide but a strategic tool for proactive adaptation and evolution in the face of DORA’s demands.
As the financial sector navigates these new regulatory waters, “Charting KELMOR” emerges as the quintessential guide for those committed to not just surviving but thriving in the age of digital operational resilience. It is a clarion call for attentiveness, alignment, and preparedness – a must-read for every financial service executive determined to lead their organization with foresight and fortitude.

```html
<!DOCTYPE html>
<html lang="en">
<head>
<meta charset="utf-8">
<title>Charting KELMOR – Front Cover</title>
<link href="https://fonts.googleapis.com/css2?family=Cinzel:wght@400;500;600;700&display=swap" rel="stylesheet">
<style>
  :root {
    --stage: #f3f3f3;
    --ocean-top: #0e4f92;
    --ocean-mid: #1765b3;
    --ocean-low: #1a4f95;
    --ocean-deep: #173d78;
    --gold-light: #fbe64a;
    --gold-mid: #f5c61e;
    --gold-deep: #e8a41b;
    --navy: #14285a;
    --white: #ffffff;
    --portrait-top: #8a6a5e;
    --portrait-low: #1b2438;
  }
  html, body {
    margin: 0;
    width: 1200px;
    height: 1060px;
    overflow: hidden;
    background: var(--stage);
  }
  .canvas {
    position: relative;
    width: 1200px;
    height: 1060px;
  }
  .cover {
    position: absolute;
    left: 280px;
    top: 50px;
    width: 640px;
    height: 960px;
    overflow: hidden;
    box-shadow: 0 6px 24px rgba(0,0,0,0.15);
    font-family: "Cinzel", serif;
  }
  .cover__backdrop {
    position: absolute;
    inset: 0;
    background: linear-gradient(180deg, var(--ocean-top) 0%, var(--ocean-mid) 45%, var(--ocean-low) 80%, var(--ocean-deep) 100%);
  }
  .cover__tagline {
    position: absolute;
    top: 38px;
    left: 0;
    right: 0;
    margin: 0;
    text-align: center;
    color: var(--white);
    font-size: 21px;
    font-weight: 400;
    line-height: 30px;
    letter-spacing: 0.5px;
  }
  .cover__title {
    margin: 0;
    font-weight: 400;
  }
  .cover__title-lead,
  .cover__title-main {
    position: absolute;
    left: 0;
    right: 0;
    text-align: center;
    white-space: nowrap;
  }
  .cover__title-lead {
    top: 128px;
    font-size: 64px;
    line-height: 80px;
    letter-spacing: 1px;
    background: linear-gradient(90deg, var(--gold-deep), var(--gold-light) 50%, var(--gold-deep));
    -webkit-background-clip: text;
    background-clip: text;
    color: transparent;
  }
  .cover__title-main {
    top: 195px;
    font-size: 138px;
    line-height: 180px;
    font-weight: 600;
    color: var(--white);
    letter-spacing: -2px;
  }
  .cover__portrait {
    position: absolute;
    left: 0;
    top: 363px;
    width: 380px;
    height: 510px;
    background: linear-gradient(180deg, var(--portrait-top) 0%, #4a4550 45%, var(--portrait-low) 70%, var(--portrait-low) 100%);
  }
  .cover__author-band {
    position: absolute;
    left: 0;
    right: 0;
    bottom: 0;
    height: 87px;
    background: linear-gradient(90deg, var(--gold-deep) 0%, var(--gold-mid) 30%, var(--gold-light) 60%, var(--gold-mid) 85%, var(--gold-deep) 100%);
    display: flex;
    align-items: center;
    justify-content: center;
  }
  .cover__author {
    margin: 0;
    color: var(--navy);
    font-size: 54px;
    font-weight: 600;
    letter-spacing: 0.5px;
    white-space: nowrap;
  }
</style>
</head>
<body>
<main class="canvas">
  <article class="cover">
    <div class="cover__backdrop" role="img" aria-label="Deep blue water texture with a dark blue road winding into the distance"></div>

    <p class="cover__tagline">A Boardroom Leader’s Field Guide<br>to Oversight and Endurance</p>

    <h1 class="cover__title">
      <span class="cover__title-lead">CHARTING</span>
      <span class="cover__title-main">KELMOR</span>
    </h1>

    <div class="cover__portrait" role="img" aria-label="Portrait photograph of the author in a dark suit and pink tie"></div>

    <div class="cover__author-band">
      <p class="cover__author">Martin J Hollis</p>
    </div>
  </article>
</main>
</body>
</html>
```